Clean Air Information

I am uploading a rough draft on what I want. I am looking for different ideas on how to make it look more attractive and not so boring. I want it to really stand out and make a statement. Also, I am uploading additional documents for statement information or additional use.

Reason: I am providing more time to ensure there is enough time for all parties.

The most recent submissions are looking good. Please keep it coming, I have extended deadline.

```html
<!DOCTYPE html>
<html lang="en">
<head>
<meta charset="utf-8">
<title>Indoor Air Quality – Meadowline Air Group</title>
<link href="https://fonts.googleapis.com/css2?family=Arimo:ital,wght@0,400;0,700;1,400&family=Archivo+Black&family=Tinos&display=swap" rel="stylesheet">
<style>
:root{
  --blue:#1a8fd6;
  --blue-dark:#0f6fb8;
  --teal:#5cc6d8;
  --green:#7cc242;
  --grey-text:#555;
  --grey-head:#6b6b6b;
  --sky-top:#5fb0e3;
  --sky-mid:#bfe1f5;
  --white:#fff;
}
*{margin:0;padding:0;box-sizing:border-box}
html,body{width:1200px;height:1198px;overflow:hidden;background:var(--white)}
body{font-family:"Arimo",Arial,sans-serif;color:var(--grey-text);position:relative}
.abs{position:absolute}
.top-wave{left:0;top:0}
.tagline-top{left:28px;top:22px;color:var(--white);font-size:17px;transform:rotate(-2.5deg);transform-origin:left}
.symptoms{left:181px;top:75px;width:385px;height:479px;border:2px solid var(--blue);border-radius:10px;padding:20px 26px 0 26px;font-size:12.4px;line-height:15px}
.symptoms-title{position:absolute;top:-10px;left:22px;background:var(--white);padding:0 6px;font-size:12.4px;color:#444}
.symptoms p{margin-bottom:15px}
.brand-left{left:40px;top:290px;width:140px}
.brand-mark{width:84px;height:84px;border-radius:50%;border:5px solid var(--green);margin-left:6px}
.brand-name{font-size:10px;font-weight:700;color:#333;margin-top:12px}
.contact{left:40px;top:442px;font-size:10px;line-height:15.5px;color:#333}
.contact .company{font-family:"Tinos",serif;font-size:16px;letter-spacing:1px;color:#333;margin-bottom:4px}
.contact .gap{height:18px}
.hero-title{left:636px;top:80px;font-family:"Archivo Black",sans-serif;font-size:29px;letter-spacing:1px;transform:rotate(2.2deg);transform-origin:left;white-space:nowrap}
.hero-title .b{color:var(--blue)} .hero-title .g{color:#8a8a8a}
.hero-scene{left:600px;top:150px}
.mini-mark{left:638px;top:438px;width:68px;height:68px;border-radius:50%;background:var(--white);box-shadow:0 1px 4px rgba(0,0,0,.3);display:flex;align-items:center;justify-content:center;text-align:center;font-size:7px;font-weight:700;color:#333;line-height:9px}
.iaq{left:618px;top:530px;font-family:"Archivo Black",sans-serif;font-size:46px;color:var(--teal);letter-spacing:1px;white-space:nowrap}
.iaq .b{color:var(--blue)}
.sky{left:0;top:600px;width:1200px;height:150px;background:linear-gradient(180deg,var(--sky-top),var(--sky-mid) 70%,var(--white))}
.face-photo{left:20px;top:614px;width:75px;height:98px;background:linear-gradient(180deg,#9fc8dc,#6fa6c4)}
.intro{left:118px;top:622px;width:440px;font-size:11.6px;line-height:15.3px;font-style:italic;color:#333;text-align:justify}
.info{left:18px;top:733px;width:562px;font-size:12px;line-height:15px;color:#333}
.info h2{font-size:12.8px;font-weight:700;color:var(--grey-head);margin:0 0 4px 22px;letter-spacing:.3px}
.info p{margin-bottom:17px}
.info ul{list-style:none}
.info li::before{content:"• "}
.offer-title{left:736px;top:616px;font-family:"Arimo",sans-serif;font-weight:700;font-size:24px;color:var(--white);letter-spacing:1px;text-shadow:0 0 2px #2a7fb8,0 1px 2px #2a7fb8}
.offer-mark{left:632px;top:625px;width:80px;height:80px}
.fan-photo{left:632px;top:690px;width:170px;height:240px;border-radius:50% 0 0 50%;background:radial-gradient(circle at 70% 50%,#f4f6f8,#b9c2ca 60%,#8f9aa5)}
.offer-box{left:736px;top:657px;width:386px;height:291px;background:var(--white);border:2px solid var(--blue);border-radius:10px;padding-top:17px;text-align:center;font-weight:700;font-size:13.4px;line-height:22px;color:#111}
.service{width:270px;font-size:12.4px;line-height:15px;color:#333}
.service h3{font-size:12.8px;color:var(--blue-dark);font-weight:700;line-height:15px}
.service-rule{border-left:2px solid var(--blue);padding-left:9px;margin-left:-11px}
.footer{left:0;top:1174px;width:1200px;height:24px;background:var(--blue)}
.footer-url{left:18px;top:1175px;color:var(--white);font-weight:700;font-size:15.5px}
.footer-tag{right:26px;top:1172px;color:var(--white);font-weight:700;font-size:19px}
</style>
</head>
<body>

<svg class="abs top-wave" width="1200" height="70" viewBox="0 0 1200 70" aria-hidden="true">
  <defs><linearGradient id="wave" x1="0" x2="1"><stop offset="0" stop-color="#1a8fd6"/><stop offset=".6" stop-color="#4fb0e6"/><stop offset="1" stop-color="#d6eefa"/></linearGradient></defs>
  <path d="M0 0H1200V8C900 12 620 30 420 45C260 56 120 62 0 60Z" fill="url(#wave)"/>
</svg>
<div class="abs tagline-top">Let us help you breathe easier</div>

<section class="abs symptoms">
  <div class="symptoms-title">Did you know what are the signs and symptoms of asthma?</div>
  <p>Asthma symptoms will vary from person to person and in fact, the same person may experience asthma symptoms differently from one episode to the next. Generally speaking, asthma symptoms include:</p>
  <p>• Wheezing. Wheezes are whistling sounds that occur with breathing when the airways are constricted. Not all wheezing is audible. Some wheezing can only be heard with a stethoscope.</p>
  <p>• Tightness in the chest. Airway inflammation and constriction make it feel like you can't take a deep enough breath or that you can't get enough air in or out. Some also describe this as if something was wrapped around the chest or someone was sitting on the chest.</p>
  <p>• Cough. Asthma triggers irritate the airways, creating a lot – and sometimes nonstop – coughing. Night time coughing, especially, is a common symptom of asthma.</p>
  <p>• Difficulty breathing. Symptoms may increase so that you feel like you cannot breathe adequately. You may be breathing more rapidly, or feel like you are not getting enough air no matter how hard you try. Mild exertion (such as walking up stairs) may become a strain.</p>
  <p>• Change in peak flow meter readings. Asthma symptoms are increasing when your peak flow meter reads in the caution or danger range.</p>
</section>

<div class="abs brand-left">
  <div class="brand-mark"></div>
  <div class="brand-name">Meadowline Air Group</div>
</div>

<address class="abs contact" style="font-style:normal">
  <div class="company">FRESH ROOM</div>
  4120 Harbor Ridge Dr<br>Suite 210-B<br>Oakvale, TX 75990
  <div class="gap"></div>
  Phone: 555-014-2288<br>Fax: 555-019-4410<br>www.meadowline-air.com
</address>

<h1 class="abs hero-title"><span class="b">CLEAN AIR</span> <span class="g">INTO</span> <span class="b">YOUR HOME</span></h1>

<svg class="abs hero-scene" width="600" height="350" viewBox="0 0 600 350">
  <defs>
    <linearGradient id="room" x1="0" y1="0" x2="0" y2="1"><stop offset="0" stop-color="#d9e9f2"/><stop offset="1" stop-color="#eef4f8"/></linearGradient>
    <linearGradient id="skyWin" x1="0" y1="0" x2="0" y2="1"><stop offset="0" stop-color="#2f74c4"/><stop offset="1" stop-color="#a9d0ef"/></linearGradient>
  </defs>
  <path d="M0 0C180 18 380 40 600 30V300C420 310 200 330 0 320Z" fill="url(#room)" role="img" aria-label="Bright living room with an open window showing blue sky and clouds"/>
  <rect x="130" y="10" width="190" height="280" fill="url(#skyWin)" role="img" aria-label="Open window framing a blue cloudy sky"/>
  <path d="M0 2C180 20 380 42 600 32" fill="none" stroke="#7cc242" stroke-width="4"/>
  <path d="M0 10C180 30 380 52 600 40" fill="none" stroke="#1a8fd6" stroke-width="3"/>
  <path d="M0 318C200 330 420 310 600 298" fill="none" stroke="#1a8fd6" stroke-width="3"/>
  <path d="M0 326C200 338 420 318 600 306" fill="none" stroke="#7cc242" stroke-width="4"/>
</svg>
<div class="abs mini-mark">Meadowline<br>Air Group</div>

<div class="abs iaq">INDOOR <span class="b">AIR</span> QUALITY</div>

<div class="abs sky"></div>
<div class="abs face-photo" role="img" aria-label="Close-up photograph in blue tones of a person breathing"></div>
<p class="abs intro">More Americans than ever before say they are suffering from allergies. In fact, the prevalence of allergies has been increasing since the early 1980s across all ages, genders, and racial groups. Allergy symptoms can vary, depending on the type of allergic disease. Although there currently is no known cure for any allergy, they generally can be managed very effectively with proper prevention and treatment.</p>

<section class="abs info">
  <h2>INDOOR AIR QUALITY AND ALLERGIES</h2>
  <p>Allergy and asthma control begins at home. Many people with allergies stay indoors when outdoor air is full of pollen and spores. But dust mites, animal dander and even cockroaches can cause problems indoors.</p>
  <h2>WHAT IS AN ALLERGY?</h2>
  <p>Allergy is a general term that describes an overreaction of the body's immune system to substances that usually cause no reaction in most people. This overreaction to allergens, or substances that cause a reaction, can result in a variety of allergy symptoms ranging from very mild to life threatening.</p>
  <h2>WHAT ARE THE MOST COMMON ALLERGIC CONDITIONS?</h2>
  <p>An allergic reaction can affect the body in various ways. Some allergic diseases are more common than others. Their names and chief characteristics are outlined below. Allergic rhinitis (hay fever) is characterized by stuffy, itchy, runny nose, sneezing, and itching of the roof of the mouth, the throat, and/or the ears.</p>
  <h2>WHAT KINDS OF SUBSTANCES ARE CONSIDERED TO BE ALLERGENS?</h2>
  <ul>
    <li style="list-style:none">The most common allergens which are known to trigger an allergic reaction include:</li>
    <li>Pollen, a substance which is part of the reproductive cycle in plants, trees, weeds, and grasses.</li>
    <li>Molds. Are classified as fungi and can be found nearly everywhere in the natural world.</li>
    <li>Animals. Protein-based substances such as saliva, dander (flaked skin), and urine trigger allergies.</li>
    <li>Bugs. The bodies and fecal material of dust mites and cockroach allergens are potent allergens.</li>
    <li>Foods. Nearly 90% of all food allergy reactions are caused by just eight foods: cow's milk, soy, eggs, wheat, peanuts, tree nuts, fish, and shellfish.</li>
    <li>Latex, sometimes called natural rubber.</li>
    <li>Drugs. Both prescription and over-the-counter medications can be allergens for sensitive people, with penicillin (and its derivatives) being the most common allergy trigger.</li>
    <li>Insect venom. Stings from bees, wasps and ants can cause an allergic response.</li>
    <li>Smoke</li>
  </ul>
</section>

<h2 class="abs offer-title">WHAT WE CAN OFFER YOU</h2>
<div class="abs mini-mark" style="left:636px;top:628px;width:74px;height:74px">Meadowline<br>Air Group</div>
<div class="abs fan-photo" role="img" aria-label="Metal ventilation fan grille"></div>
<div class="abs offer-box">
  HVAC Inspection<br>Mold Testing<br>Air Duct Cleaning<br>Contaminant Removal<br>Air Quality Assessment and Protocol<br>Mold Mitigation and Remediation<br>HVAC Remediation/Replacement<br>Water and Fire Damage Restoration<br>Reconstruction<br>Catastrophe Relief Coordination<br>After Hours Emergency Service<br>Insurance Advocate Services
</div>

<div class="abs service service-rule" style="left:628px;top:959px"><h3>Inspection and Testing</h3>A thorough inspection is performed and samples are taken and sent out for 3rd party testing to determine category and severity level.</div>
<div class="abs service" style="left:628px;top:1034px"><h3>Dehumidification</h3>Any standing water or water damage in your home is cleaned out and all affected areas are thoroughly dried.</div>
<div class="abs service" style="left:628px;top:1108px"><h3>Containment</h3>Chambers can be placed around localized areas to prevent any further migration until the areas have been thoroughly decontaminated.</div>
<div class="abs service service-rule" style="left:918px;top:959px"><h3>Removal and Replacement</h3>If any components cannot be restored, they will be safely removed from the premises and replaced.</div>
<div class="abs service" style="left:918px;top:1034px"><h3>Disinfection</h3>A detailed cleaning and disinfection of all the components and ductwork within your system will be performed.</div>
<div class="abs service" style="left:918px;top:1109px"><h3>Confirmation</h3>Retest of the system and the air in your home to verify that the contaminants have been eradicated.</div>

<div class="abs footer"></div>
<div class="abs footer-url">www.meadowline-air.com</div>
<div class="abs footer-tag">Let us help you breathe easier</div>

</body>
</html>
```